Improving a camping website homepage header*

My client is very happy with his new website and its new functionalities. However, he's not very happy about the homepage design. Specifically, the header(this includes the menu, large header image and two columns beneath that). You can find the website here: http://lnkvo.example/siteTentra .

He forwarded me several other websites he likes. Which can be found in the attachments. I also included several pictures of the camping.

I'm looking for a design that will improve the header of the homepage with room for other global style chances. The logo cannot be changed.

Attachments
1) His old website homepage
2) Website mockup he liked.
3) Another website mockup he liked.

Other images can be found on the new website http://lnkvo.example/siteTentra or his old website http://lnkvo.example/formerSiteTentra.

Can you help us?
Updates

Hello guys. Here's a bit more information - Language used on the website is dutch. - The two columns left/right are supposed to link to Hire/Buy chalets. The client indicated that he finds these links important, but doesn't like the current design. I think this is partially the case because he doesn't like the icons. I'm looking forward to your designs!

Target Market(s)

30-50 year old wealthy people that want to purchase or rent cabins in the Netherlands.

Number of Pages Required

1 page

Colors

Designer to choose colors to be used in the design.

Requirements
Must have
• Improved header
Nice to have
• Global style changes
Should not have
• Logo changes

```html
<!DOCTYPE html>
<html lang="nl">
<head>
<meta charset="utf-8">
<title>Parc Veldenrust</title>
<link href="https://fonts.googleapis.com/css2?family=Poppins:wght@400;500;600;700&family=Roboto:wght@400;500;700&family=Roboto+Condensed:wght@700&display=swap" rel="stylesheet">
<style>
:root{
  --green:#4c9a1f;--green-light:#6cbf2e;--blue:#2e7fbf;--nav-blue:#3a87c4;
  --orange:#f28a1a;--tag:#e7a45d;--cream:#f5f1e6;--ink:#333;--muted:#777;
  --footer:#2c3035;--footer-bar:#33373c;--line:#e6e6e6;
}
*{box-sizing:border-box;margin:0;padding:0}
html,body{width:698px;height:1200px;overflow:hidden;background:#fff}
body{position:relative;font-family:Roboto,sans-serif;color:var(--ink)}
.abs{position:absolute}
/* header */
.brand{left:76px;top:20px;display:flex;align-items:center;gap:6px}
.brand-dot{width:28px;height:28px;border-radius:50%;background:var(--green-light)}
.brand-name{font-family:Poppins,sans-serif;font-weight:500;font-size:16px;color:var(--green)}
.call{left:404px;top:26px;display:flex;gap:6px;align-items:center}
.call-icon{width:24px;height:24px;border-radius:50%;border:2px solid var(--blue);display:flex;align-items:center;justify-content:center}
.call-num{font-size:11.5px;color:var(--blue);line-height:13px}
.call-mail{font-size:8.5px;color:#555}
.login{left:546px;top:25px;width:73px;height:22px;border-radius:11px;background:var(--orange);color:#fff;font-weight:500;font-size:11px;display:flex;align-items:center;justify-content:center;box-shadow:0 2px 3px rgba(0,0,0,.2)}
.nav{left:0;top:79px;width:698px;height:26px;background:linear-gradient(#72c431,#4f9d1d)}
.nav-home{position:absolute;left:77px;top:0;width:41px;height:26px;background:var(--nav-blue);display:flex;align-items:center;justify-content:center}
.nav a{position:absolute;top:0;height:26px;line-height:26px;color:#fff;font-size:8.5px;font-weight:700;text-decoration:none;border-left:1px solid rgba(255,255,255,.18);padding-left:14px}
/* hero */
.hero{left:0;top:105px;width:698px;height:301px;background:linear-gradient(180deg,#7f9a6b 0%,#8a6a4a 45%,#4e6b34 100%)}
.hero-title{left:228px;top:207px;width:242px;height:72px;border:2px solid #fff;border-radius:9px;background:rgba(30,30,30,.7);color:#fff;text-align:center;font-family:'Roboto Condensed',sans-serif}
.hero-title h1{font-size:26px;margin-top:7px;letter-spacing:.3px}
.hero-title p{font-size:16px;margin-top:2px;font-family:Roboto,sans-serif}
.panel{left:63px;top:366px;width:572px;height:160px;background:#fff;border-radius:12px 12px 0 0}
.card{top:380px;width:264px;height:133px;background:var(--cream);box-shadow:0 0 5px rgba(0,0,0,.25);border:2px solid #fff;overflow:hidden}
.card-body{position:absolute;left:145px;top:16px;width:112px}
.card-body h2{font-size:11.5px;font-weight:500;color:#222;margin-bottom:8px}
.card-body p{font-size:6.8px;line-height:13px;color:#444}
.card-btn{display:inline-block;margin-top:8px;border:1px solid #222;border-radius:8px;font-size:6.5px;padding:3px 8px}
/* welcome */
.welcome{left:0;top:560px;width:698px;text-align:center;font-family:Poppins,sans-serif;font-weight:600;font-size:20px;letter-spacing:1px;color:#333}
.welcome span{color:var(--green)}
.intro{left:74px;top:597px;width:550px;text-align:center;font-family:Poppins,sans-serif;font-size:7.4px;line-height:15.3px;color:#333}
.section-title{left:0;top:698px;width:698px;text-align:center;font-family:Poppins,sans-serif;font-weight:600;font-size:16px;letter-spacing:.8px}
/* listings */
.listing{top:746px;width:175px;height:208px;border:1px solid var(--line);background:#fff}
.listing-photo{height:109px;position:relative}
.tag{position:absolute;top:10px;font-size:6px;color:#fff;padding:1px 6px}
.tag-featured{left:10px;background:var(--tag)}
.tag-type{right:10px;background:var(--blue)}
.listing-info{padding:10px 10px 0}
.listing-info h3{font-size:10px;font-weight:400;color:#333}
.price{font-size:8.5px;color:var(--orange);margin-top:6px}
.note{font-size:6.3px;color:#666;margin-top:7px}
.specs{display:flex;align-items:center;font-size:6.3px;color:#666;margin-top:5px;gap:8px}
.more{margin-left:auto;background:var(--tag);color:#fff;padding:1px 5px}
.listing-foot{position:absolute;left:10px;right:10px;bottom:10px;border-top:1px solid var(--line);padding-top:7px;display:flex;align-items:center;gap:6px;font-size:6.6px;color:var(--blue)}
.avatar{width:14px;height:14px;border-radius:50%;background:#7b8a6a}
.acts{margin-left:auto;display:flex;gap:3px}
.acts i{width:15px;height:13px;border:1px solid var(--line);display:block}
/* footer */
.footer{left:0;top:1020px;width:698px;height:153px;background:var(--footer)}
.footer h4{position:absolute;top:26px;font-size:7px;font-weight:400;color:#fff}
.f-list{position:absolute;left:90px;top:40px;font-size:6.2px;color:#bbb;line-height:14px;list-style:none}
.f-list li{padding-left:12px;position:relative}
.f-list li::before{content:"";position:absolute;left:0;top:5px;width:5px;height:5px;background:#8a8f95}
.f-chalet{position:absolute;left:267px;width:150px;height:33px}
.f-thumb{position:absolute;left:0;top:0;width:49px;height:33px;background:linear-gradient(#8ea7b8,#5d7d48)}
.f-chalet p{position:absolute;left:55px;font-size:6.2px;color:#bbb}
.f-chalet .fp{color:var(--orange)}
.socials{position:absolute;left:444px;top:48px;display:grid;grid-template-columns:repeat(6,16px);gap:8px 7.6px}
.socials span{width:16px;height:16px;border-radius:50%;background:#4a4f55;display:block}
.footbar{left:0;top:1173px;width:698px;height:27px;background:var(--footer-bar);font-size:6px;color:#aaa;padding:12px 90px}
</style>
</head>
<body>
<header>
  <div class="abs brand"><span class="brand-dot"></span><span class="brand-name">Parc Veldenrust</span></div>
  <div class="abs call">
    <span class="call-icon"><svg width="11" height="11" viewBox="0 0 24 24"><path fill="#2e7fbf" d="M6.6 10.8a15.1 15.1 0 0 0 6.6 6.6l2.2-2.2c.3-.3.7-.4 1-.2 1.1.4 2.3.6 3.6.6.6 0 1 .4 1 1V20c0 .6-.4 1-1 1A17 17 0 0 1 3 4c0-.6.4-1 1-1h3.5c.6 0 1 .4 1 1 0 1.3.2 2.5.6 3.6.1.3 0 .7-.2 1z"/></svg></span>
    <div><div class="call-num">0300 - 12 34 56</div><div class="call-mail">info@parcveldenrust.nl</div></div>
  </div>
  <div class="abs login">Inloggen</div>
</header>
<nav class="abs nav">
  <span class="nav-home"><svg width="12" height="11" viewBox="0 0 24 22"><path fill="#fff" d="M12 1 1 11h3v10h6v-6h4v6h6V11h3z"/></svg></span>
  <a style="left:122px;border-left:0">HET PARK</a>
  <a style="left:190px">FINANCIERING</a>
  <a style="left:275px">CHALETS</a>
  <a style="left:341px">AANBIEDINGEN</a>
  <a style="left:430px">FACILITEITEN</a>
  <a style="left:511px">CONTACT</a>
</nav>
<section class="abs hero" role="img" aria-label="Foto van een houten chalet tussen groene bomen"></section>
<svg class="abs" style="left:52px;top:225px" width="16" height="32" viewBox="0 0 16 32"><path d="M14 2 2 16l12 14" stroke="#fff" stroke-width="1.5" fill="none"/></svg>
<svg class="abs" style="left:628px;top:225px" width="16" height="32" viewBox="0 0 16 32"><path d="M2 2l12 14L2 30" stroke="#fff" stroke-width="1.5" fill="none"/></svg>
<div class="abs hero-title"><h1>PARC VELDENRUST</h1><p>&#9742; 0300 – 12 34 56</p></div>
<div class="abs panel"></div>

<div class="abs card" style="left:76px">
  <svg class="abs" style="left:0;top:0" width="150" height="133" role="img" aria-label="Foto van een chalet in blauwe tint"><path d="M0 0H128C108 30 140 70 118 100 112 112 122 124 132 133H0Z" fill="#3d7ea0"/><g fill="none" stroke="#fff" stroke-width="2"><path d="M40 75 58 60 76 75M45 72v24h26V72M52 96V84h8v12"/></g></svg>
  <div class="card-body"><h2>CHALET HUREN</h2><p>Lorem ipsum dolor sit amet, consectetur adipiscing elit. Aenean euismod bibendum laoreet. Proin gravida dolor sit amet lacus</p><span class="card-btn">Read More</span></div>
</div>
<div class="abs card" style="left:358px">
  <svg class="abs" style="left:0;top:0" width="150" height="133" role="img" aria-label="Foto van een chalet in groene tint"><path d="M0 0H128C108 30 140 70 118 100 112 112 122 124 132 133H0Z" fill="#4e9c25"/><g fill="none" stroke="#fff" stroke-width="2.5"><rect x="42" y="60" width="36" height="18" rx="2"/><circle cx="60" cy="69" r="5"/><path d="M42 84h36M42 90h36"/></g></svg>
  <div class="card-body"><h2>CHALET KOPEN</h2><p>Lorem ipsum dolor sit amet, consectetur adipiscing elit. Aenean euismod bibendum laoreet. Proin gravida dolor sit amet lacus</p><span class="card-btn">Read More</span></div>
</div>

<h2 class="abs welcome">WELCOME TO <span>PARC VELDENRUST</span></h2>
<p class="abs intro">Sed ut perspiciatis unde omnis iste natus error sit voluptatem accusantium doloremque laudantium, totam rem aperiam, eaque ipsa quae ab illo inventore veritatis et quasi architecto beatae vitae dicta sunt explicabo. Nemo enim ipsam voluptatem quia voluptas sit aspernatur aut odit aut fugit, sed quia consequuntur magni dolores eos qui ratione voluptatem sequi nesciunt. Neque porro quisquam est, qui dolorem ipsum quia dolor sit amet, consectetur, adipisci velit, sed quia non numquam eius modi tempora incidunt ut labore et dolore magnam aliquam quaerat voluptatem.</p>
<h2 class="abs section-title">RECENTE CHALETS</h2>

<article class="abs listing" style="left:71px">
  <div class="listing-photo" role="img" aria-label="Foto van chalet Kavel 190" style="background:linear-gradient(#9fb3c4,#6f7a6a 60%,#4f6b37)"><span class="tag tag-featured">Aanbevolen</span><span class="tag tag-type">Huren</span></div>
  <div class="listing-info"><h3>Kavel 190</h3><div class="price">€ 350 per maand</div><div class="specs"><span>▭ 1</span><span>▭ 3</span><span>▭ 105 000,00 m²</span><span class="more">lees meer</span></div></div>
  <div class="listing-foot"><span class="avatar"></span>admin<span class="acts"><i></i><i></i><i></i></span></div>
</article>
<article class="abs listing" style="left:260px">
  <div class="listing-photo" role="img" aria-label="Foto van chalet Kavel 233 aan het water" style="background:linear-gradient(#8fa68a,#c8cfc4 50%,#3f6a2d)"><span class="tag tag-featured">Aanbevolen</span><span class="tag tag-type" style="right:60px">Kopen</span></div>
  <div class="listing-info"><h3>Kavel 233</h3><div class="price">€ 205.000</div><div class="note">Ook een mooie chalet.</div><div class="specs"><span>▭ 1</span><span>▭ 1</span><span>▭ 130,00 m²</span><span class="more">lees meer</span></div></div>
  <div class="listing-foot"><span class="avatar"></span>admin<span class="acts"><i></i><i></i><i></i></span></div>
</article>
<article class="abs listing" style="left:450px">
  <div class="listing-photo" role="img" aria-label="Foto van houten chalet Kavel 236" style="background:linear-gradient(#a9b9c5,#9a5a30 55%,#5b5b55)"><span class="tag tag-featured">Aanbevolen</span><span class="tag tag-type">Kopen</span></div>
  <div class="listing-info"><h3>Kavel 236</h3><div class="price">€ 195.000</div><div class="note">Prachtige locatie incl. video!</div><div class="specs"><span>▭ 3</span><span>▭ 2</span><span>▭ 100,00 m²</span><span class="more">lees meer</span></div></div>
  <div class="listing-foot" style="color:#555"><span class="avatar" style="background:#ccc"></span>Naam Achternaam<span class="acts"><i></i><i></i><i></i></span></div>
</article>

<footer class="abs footer">
  <h4 style="left:90px">Contact</h4>
  <ul class="f-list">
    <li>Hoeveweg 14b<br>4100 AB Lindendal</li>
    <li>0300 - 12 34 56</li>
    <li>0300 - 12 34 57</li>
    <li>info@parcveldenrust.nl</li>
    <li>parcVeldenrustChat</li>
    <li>http://parc-veldenrust.nl</li>
  </ul>
  <h4 style="left:267px">Nieuwe Chalets</h4>
  <div class="f-chalet" style="top:40px"><span class="f-thumb" role="img" aria-label="Foto Kavel 190"></span><p style="top:4px">Kavel 190</p><p class="fp" style="top:14px">€ 350 per maand</p></div>
  <div class="f-chalet" style="top:78px"><span class="f-thumb" role="img" aria-label="Foto Kavel 233"></span><p style="top:4px">Kavel 233</p><p class="fp" style="top:14px">€ 205.000</p></div>
  <h4 style="left:444px">Sociale media</h4>
  <div class="socials"><span></span><span></span><span></span><span></span><span></span><span></span><span></span><span></span><span></span><span></span><span></span><span></span></div>
</footer>
<div class="abs footbar">Copyright 2018 | Parc Veldenrust</div>
</body>
</html>
```